Product Sales Website Design - E-commerce - Shopify etc

We have been selling printing equipment for some time now and think that it will be useful to sell the products on the internet, using a simple e-commerce platform, such as shopify etc. There are roughly a few dozen products - so basically, the idea is to have a modern, simple and clean home page. When someone looks at it, they think, this is it - I want to buy here. I am not going to impose any ideas or say how I want it done.

Just so you know, at the moment there are three categories of products. One being printers, scanners and accessories.

I am excited by this whole project and don't want to have good designers backing out because they feel i am imposing restrictions. Feel free to impress me.

Industry/Entity Type

E-Commerce

Requirements
Must have
• integration with an e-commerce platform is a must or show how to integrate, so I can easily introduce further products.

```html
<!DOCTYPE html>
<html lang="en">
<head>
<meta charset="utf-8">
<title>Company Name — Printers, Scanners &amp; Accessories</title>
<link rel="stylesheet" href="https://fonts.googleapis.com/css2?family=Arimo:wght@400&family=Pathway+Gothic+One&display=swap">
<style>
  :root {
    --brand-blue: #1a56a8;
    --button-blue: #0e4f9c;
    --nav-grey: #5b6b7c;
    --heading-ink: #231f1c;
    --body-ink: #2a2a2a;
    --hero-light: #fdfcf4;
    --hero-mid: #f0e7bd;
    --hero-deep: #dfcd80;
    --dot-grey: #7c7572;
    --visual-light: #f6f6f6;
    --visual-mid: #e4e4e4;
    --visual-deep: #cfcfcf;
    --footer-bg: #232529;
    --footer-ink: #d9d9d9;
    --white: #ffffff;
  }
  * { box-sizing: border-box; margin: 0; padding: 0; }
  html, body { width: 1200px; height: 855px; overflow: hidden; background: var(--white); }
  body { position: relative; font-family: "Arimo", Arial, sans-serif; }

  .site-header { position: absolute; inset: 0 0 auto 0; height: 145px; }
  .brand {
    position: absolute; left: 206px; top: 46px;
    font-family: "Arimo", Arial, sans-serif; font-size: 43px; font-weight: 400;
    color: var(--brand-blue); letter-spacing: -0.3px;
  }
  .account-links {
    position: absolute; right: 205px; top: 19px;
    font-family: "Pathway Gothic One", "Arial Narrow", sans-serif;
    font-size: 14px; color: var(--brand-blue); display: flex; gap: 10px;
  }
  .account-links a { color: inherit; text-decoration: none; }
  .main-nav {
    position: absolute; right: 205px; top: 62px; display: flex; gap: 22px;
    font-family: "Pathway Gothic One", "Arial Narrow", sans-serif; font-size: 22px;
  }
  .main-nav a { color: var(--nav-grey); text-decoration: none; }

  .hero {
    position: absolute; left: 0; top: 145px; width: 1200px; height: 322px;
    background: radial-gradient(ellipse 520px 330px at 456px 176px,
      var(--hero-light) 0%, var(--hero-mid) 45%, var(--hero-deep) 100%);
  }
  .hero-copy { position: absolute; left: 254px; top: 68px; width: 320px; text-align: center; }
  .hero-title {
    font-family: "Pathway Gothic One", "Arial Narrow", sans-serif;
    font-size: 60px; line-height: 56px; color: var(--heading-ink); font-weight: 400;
  }
  .hero-subtitle {
    font-family: "Pathway Gothic One", "Arial Narrow", sans-serif;
    font-size: 34px; line-height: 34px; color: var(--heading-ink); font-weight: 400;
  }
  .hero-button {
    position: absolute; left: 314px; top: 192px; width: 177px; height: 59px;
    background: var(--button-blue); border: 2px solid var(--white); border-radius: 4px;
    color: var(--white); text-decoration: none;
    font-family: "Pathway Gothic One", "Arial Narrow", sans-serif; font-size: 31px;
    display: flex; align-items: center; justify-content: center;
  }
  .slider-dots { position: absolute; left: 374px; top: 286px; display: flex; gap: 6px; }
  .slider-dots span { width: 11px; height: 11px; border-radius: 50%; background: var(--dot-grey); }
  .slider-dots span.is-active { background: var(--button-blue); }

  .hero-product {
    position: absolute; left: 628px; top: 160px; width: 350px; height: 349px;
    border-radius: 14px;
    background: linear-gradient(180deg, var(--visual-light) 0%, var(--visual-mid) 60%, var(--visual-deep) 100%);
  }

  .category { position: absolute; top: 514px; }
  .category-visual {
    position: absolute; left: 0; top: 0; width: 148px; height: 132px; border-radius: 8px;
    background: linear-gradient(180deg, var(--visual-light), var(--visual-deep));
  }
  .category-title {
    position: absolute; top: 150px; left: 0;
    font-family: "Pathway Gothic One", "Arial Narrow", sans-serif;
    font-size: 28px; font-weight: 400; color: var(--heading-ink); line-height: 32px;
  }
  .category-text {
    position: absolute; top: 186px; left: 0; width: 100%;
    font-size: 10.5px; line-height: 17px; color: var(--body-ink);
    text-align: justify; height: 85px; overflow: hidden;
  }
  .category--printers { left: 173px; width: 261px; }
  .category--scanners { left: 466px; width: 257px; }
  .category--accessories { left: 753px; width: 251px; }

  .site-footer {
    position: absolute; left: 0; top: 824px; width: 1200px; height: 31px;
    background: var(--footer-bg); color: var(--footer-ink);
    font-size: 10.5px; display: flex; align-items: center; justify-content: center;
    border-top: 1px solid #111;
  }
</style>
</head>
<body>
  <header class="site-header">
    <div class="brand">Company Name</div>
    <div class="account-links"><a href="#">LOGIN</a><span>|</span><a href="#">CART</a></div>
    <nav class="main-nav">
      <a href="#">PRODUCTS</a><a href="#">SERVICES</a><a href="#">ABOUT</a><a href="#">CONTACT</a>
    </nav>
  </header>

  <section class="hero">
    <div class="hero-copy">
      <h1 class="hero-title">BUY PRINTERS</h1>
      <p class="hero-subtitle">BEST QUALITY</p>
    </div>
    <a class="hero-button" href="#">LEARN MORE</a>
    <div class="slider-dots"><span></span><span></span><span class="is-active"></span></div>
  </section>
  <div class="hero-product" role="img" aria-label="Illustration of a white desktop printer printing cyan, magenta, yellow and black stripes"></div>

  <main class="categories">
    <article class="category category--printers">
      <div class="category-visual" role="img" aria-label="Printer icon"></div>
      <h2 class="category-title">Printers</h2>
      <p class="category-text">Lorem ipsum dolor sit amet, consectetur adipiscing elit. Sed at ante. Mauris eleifend, quam a vulputate dictum, massa quam dapibus leo, eget vulputate orci purus ut lorem. In fringilla mi in ligula. Pellentesque aliquam quam vel dolor. Nunc adipiscing. Sed quam odio, suscipit a, pretium in, interdum non.</p>
    </article>
    <article class="category category--scanners">
      <div class="category-visual" role="img" aria-label="Flatbed scanner icon"></div>
      <h2 class="category-title">Scanners</h2>
      <p class="category-text">Lorem ipsum dolor sit amet, consectetur adipiscing elit. Sed at ante. Mauris eleifend, quam a vulputate dictum, massa quam dapibus leo, eget vulputate orci purus ut lorem. In fringilla mi in ligula. Pellentesque aliquam quam vel dolor. Nunc adipiscing. Sed quam odio, suscipit a, pretium in, interdum non.</p>
    </article>
    <article class="category category--accessories">
      <div class="category-visual" role="img" aria-label="Open box of accessories with cables, a disc and a circuit board"></div>
      <h2 class="category-title">Accessories</h2>
      <p class="category-text">Lorem ipsum dolor sit amet, consectetur adipiscing elit. Sed at ante. Mauris eleifend, quam a vulputate dictum, massa quam dapibus leo, eget vulputate orci purus ut lorem. In fringilla mi in ligula. Pellentesque aliquam quam vel dolor. Nunc adipiscing. Sed quam odio, suscipit a, pretium in.</p>
    </article>
  </main>

  <footer class="site-footer">Copyright 2014 Company name - Terms &amp; Conditions | Privacy Policy</footer>
</body>
</html>
```